Personal Injury Law Firm needs folder design

Need a folder design for our personal injury law firm, Torrin & Mapley, LLC. to give to all of our clients with their documents at the end of their case. I've attached our branding guide. We are branded as the 5 star law firm that fights for our clients like family. It should incorporate our colors or Green and White. We'd like to convey a message of moving on to the next chapter after finishing their case.

```html
<!DOCTYPE html>
<html lang="en">
<head>
<meta charset="utf-8">
<title>Torrin &amp; Mapley, LLC. — Client Folder</title>
<link rel="stylesheet" href="https://fonts.googleapis.com/css2?family=Cinzel:wght@500&family=Open+Sans:wght@400;700&display=swap">
<style>
  :root {
    --bg: #f4f4f4;
    --folder-dark: #1b3138;
    --folder-dark-edge: #223b42;
    --green: #3fae85;
    --green-light: #4cb891;
    --green-deep: #35a07a;
    --paper: #ffffff;
    --ink: #2a2a2a;
    --white: #ffffff;
  }
  * { box-sizing: border-box; margin: 0; padding: 0; }
  html, body { width: 1200px; height: 1200px; overflow: hidden; }
  body { background: var(--bg); font-family: "Open Sans", sans-serif; }
  .canvas { position: relative; width: 1200px; height: 1200px; }

  .folder-inside {
    position: absolute; left: 70px; top: 260px; width: 500px; height: 680px;
    background: var(--folder-dark); overflow: hidden;
    box-shadow: 0 18px 40px rgba(0,0,0,.15);
  }
  .letter {
    position: absolute; left: 45px; top: 34px; width: 410px; height: 600px;
    background: var(--paper); padding: 28px 34px; color: var(--ink);
    font-size: 10.5px; line-height: 1.45;
  }
  .letter-brand { display: flex; align-items: center; gap: 8px; margin-bottom: 34px; }
  .brand-square { width: 26px; height: 26px; background: var(--green); flex: none; }
  .letter-brand .brand-name {
    font-family: "Cinzel", serif; font-weight: 500; font-size: 15px; color: var(--green);
  }
  .letter-date { margin-bottom: 14px; }
  .letter-to { font-weight: 700; }
  .letter-address { margin-bottom: 22px; font-size: 9.5px; }
  .letter p { margin-bottom: 10px; }

  .pocket { position: absolute; left: 0; top: 0; width: 500px; height: 680px; }

  .folder-cover {
    position: absolute; left: 630px; top: 260px; width: 500px; height: 680px;
    background: linear-gradient(160deg, var(--green-light) 0%, var(--green) 55%, var(--green-deep) 100%);
    box-shadow: 0 18px 40px rgba(0,0,0,.15);
    display: flex; align-items: center; justify-content: center;
  }
  .cover-texture { position: absolute; inset: 0;
    background: linear-gradient(135deg, rgba(255,255,255,.06), rgba(255,255,255,0) 60%); }
  .cover-brand { position: relative; display: flex; align-items: center; gap: 16px; margin-top: -80px; }
  .cover-brand .brand-square { width: 58px; height: 58px; background: var(--white); }
  .cover-brand .brand-name {
    font-family: "Cinzel", serif; font-weight: 500; font-size: 30px; color: var(--white); white-space: nowrap;
  }
</style>
</head>
<body>
<main class="canvas">
  <section class="folder-inside">
    <article class="letter">
      <div class="letter-brand">
        <span class="brand-square"></span>
        <span class="brand-name">Torrin &amp; Mapley, LLC.</span>
      </div>
      <div class="letter-date">Client copy</div>
      <div class="letter-to">Letter To:</div>
      <div class="letter-address">Client name, street address,<br>city and state</div>
      <p>Thank you for trusting our team with your case. It has been an honor to stand beside you and your family through every step of the process.</p>
      <p>Enclosed you will find the final documents for your records. Please keep them in a safe place.</p>
      <p>As you begin this next chapter, know that our door stays open whenever you need guidance or a friendly voice.</p>
      <p>With gratitude and warm wishes for the road ahead.</p>
    </article>
    <svg class="pocket" viewBox="0 0 500 680" aria-hidden="true">
      <path d="M0 680 V420 Q0 395 25 395 H60 Q80 395 95 430 L120 470 V680 Z" fill="var(--folder-dark-edge)"/>
      <path d="M500 140 Q420 140 400 170 V500 L60 540 V680 H500 Z" fill="var(--folder-dark-edge)"/>
      <path d="M60 540 L400 500 V510 L60 550 Z" fill="rgba(0,0,0,.12)"/>
    </svg>
  </section>

  <section class="folder-cover">
    <div class="cover-texture" role="img" aria-label="Faint geometric line pattern across the green cover"></div>
    <div class="cover-brand">
      <span class="brand-square"></span>
      <span class="brand-name">Torrin &amp; Mapley, LLC.</span>
    </div>
  </section>
</main>
</body>
</html>
```